Instagram Posts for a restaurants

We need 5-10 Instagram posts for a restaurant located in Dubai, UAE.

Background about the restaurant:

Crumbs and Kettles is a boutique burgers and comfort food joint located at Dubai, UAE. We started operations in September 2016. The main focus on our food is for it to be simple, original and freshly made. The majority of our orders are take away with fewer people opting for dinning in. We connect with our customers through our Instagram account & our customers rely on it for updates.

The brief

What we are looking for is a vector design (advertisement) for multiple purposes including:

1. announcing that we started delivery
2. a post that we can use multiple times during the year just as a "reminder that we deliver"
3. posts that serve as an advertisement

posts need to be as simple as possible

for reference, our Instagram account is @crumbsandkettles

Industry/Entity Type

Restaurant

Colors
f04a50
ffffff
000000

Requirements
Should not have
• the designs should not have too many colors

```html
<!DOCTYPE html>
<html lang="en">
<head>
<meta charset="utf-8">
<title>Crumbs and Kettles – social posts</title>
<link rel="stylesheet" href="https://fonts.googleapis.com/css2?family=Baloo+2:wght@600&display=swap">
<style>
  :root {
    --brand-red: #f04a50;
    --ink: #000000;
    --paper: #ffffff;
    --backdrop: #d8d8d8;
    --icon-tone: #1e1e1e;
  }
  * { margin: 0; padding: 0; box-sizing: border-box; }
  html, body { width: 1200px; height: 1200px; overflow: hidden; }
  body { background: var(--backdrop); position: relative; font-family: "Baloo 2", sans-serif; }

  .post {
    position: absolute;
    width: 264px;
    height: 264px;
    background: var(--paper);
    box-shadow: 0 6px 14px rgba(0,0,0,0.12);
    display: flex;
    flex-direction: column;
    align-items: center;
    justify-content: center;
    gap: 16px;
  }
  .post--delivery { left: 157px; top: 184px; }
  .post--cone     { left: 457px; top: 184px; }
  .post--life     { left: 759px; top: 184px; gap: 10px; }
  .post--chef     { left: 303px; top: 711px; }
  .post--fresh    { left: 605px; top: 711px; }

  .post__icon {
    display: block;
    background: var(--icon-tone);
    border-radius: 8px;
  }
  .post__icon--wide  { width: 94px; height: 44px; }
  .post__icon--tall  { width: 42px; height: 78px; }
  .post__icon--block { width: 56px; height: 50px; }
  .post__icon--head  { width: 56px; height: 60px; }
  .post__icon--torch { width: 34px; height: 92px; }

  .post__line {
    color: var(--brand-red);
    font-weight: 600;
    text-align: center;
    line-height: 1.02;
    font-size: 38px;
  }
  .post__line--small { font-size: 34px; line-height: 0.86; }
</style>
</head>
<body>
  <section class="post post--delivery">
    <span class="post__icon post__icon--wide" role="img" aria-label="Icon of a burger speeding along with motion lines"></span>
    <p class="post__line">we deliver<br>to you</p>
  </section>

  <section class="post post--cone">
    <span class="post__icon post__icon--tall" role="img" aria-label="Icon of fries in a paper cone"></span>
    <p class="post__line">simple<br>original</p>
  </section>

  <section class="post post--life">
    <span class="post__icon post__icon--block" role="img" aria-label="Icon of a burger with a bite taken out"></span>
    <p class="post__line post__line--small">when life<br>throws<br>you a burger<br>eat it</p>
  </section>

  <section class="post post--chef">
    <span class="post__icon post__icon--head" role="img" aria-label="Black mascot icon"></span>
    <p class="post__line">simple<br>original</p>
  </section>

  <section class="post post--fresh">
    <span class="post__icon post__icon--torch" role="img" aria-label="Icon of a grill spatula with flames above it"></span>
    <p class="post__line">freshly<br>made</p>
  </section>
</body>
</html>
```